Quarterly Growth Letter needs a Letterhead

Our firm, BRV Solutions produces "Tobias's Quarterly Growth Letter", a monthly digest of marketing tips and tips for business owners in the MENA region. We use Postlyne to distribute this memo to our database each month. We are looking for a designer to put together a letterhead for this memo.

The goal of the memo is to produce original, relevant, and new content to readers. We are a quickly adapting company. We provide fresh material, and the branding and logo of the newsletter heading should reflect this.

What the letterhead should include:
- Our BRV Solutions logo (provided by me)
- The words "Tobias's Quarterly Growth Letter"
- Tobias's picture (provided by me)

It should be in a jpg or png format so that I can load it into the Postlyne template. The template is designed to be a traditional A4 in width.

To receive our logo and Tobias's picture for your design, please email me at jordan@brvsolutions.example.

Target Market(s)

Companies in the MENA region that are looking to dramatically improve their sales and marketing.

Industry/Entity Type

Marketing

Requirements
Must have
• The letterhead must be neat and have a clean design.
Should not have
• Too many colors, swirls or soft fonts.

```html
<!DOCTYPE html>
<html lang="en">
<head>
<meta charset="utf-8">
<title>Tobias's Quarterly Growth Letter</title>
<link href="https://fonts.googleapis.com/css2?family=Roboto:wght@400;500;700&display=swap" rel="stylesheet">
<style>
  :root {
    --page: #ffffff;
    --accent-blue: #1a9ad6;
    --title-blue: #1f5a86;
    --text-grey: #5a5a5a;
    --text-dark: #3a3a3a;
    --rule-grey: #d4d4d4;
    --photo-tone-a: #e9ddd0;
    --photo-tone-b: #3a3d48;
  }
  * { margin: 0; padding: 0; box-sizing: border-box; }
  html, body { width: 849px; height: 1200px; overflow: hidden; background: var(--page); }
  .letterhead {
    position: relative;
    width: 849px;
    height: 1200px;
    background: var(--page);
    font-family: "Roboto", Arial, sans-serif;
  }
  .corner-accent { position: absolute; left: 76px; top: 99px; }
  .portrait-frame {
    position: absolute;
    left: 110px; top: 134px;
    width: 199px; height: 258px;
    background: var(--page);
    box-shadow: 0 1px 6px rgba(0,0,0,0.28);
    padding: 12px;
  }
  .portrait {
    width: 100%; height: 100%;
    background: linear-gradient(180deg, var(--photo-tone-a) 0%, var(--photo-tone-a) 45%, var(--photo-tone-b) 100%);
  }
  .masthead { position: absolute; left: 338px; top: 306px; }
  .masthead-kicker {
    font-weight: 400;
    font-size: 21px;
    letter-spacing: 4.2px;
    color: var(--text-grey);
    line-height: 1;
  }
  .masthead-title {
    margin-top: 8px;
    font-weight: 400;
    font-size: 40px;
    letter-spacing: 2.4px;
    color: var(--title-blue);
    line-height: 1;
  }
  .footer-rule {
    position: absolute;
    left: 50px; top: 1021px;
    width: 750px; height: 2px;
    background: linear-gradient(90deg, rgba(212,212,212,0) 0%, var(--rule-grey) 20%, var(--rule-grey) 80%, rgba(212,212,212,0) 100%);
  }
  .brand {
    position: absolute;
    left: 78px; top: 1066px;
    display: flex; align-items: center; gap: 12px;
  }
  .brand-dot { width: 18px; height: 18px; border-radius: 50%; background: var(--accent-blue); }
  .brand-name {
    font-weight: 400;
    font-size: 26px;
    color: var(--title-blue);
    line-height: 1;
    letter-spacing: 0.5px;
  }
  .contact {
    position: absolute;
    right: 78px; top: 1056px;
    text-align: right;
    font-style: normal;
    color: var(--text-grey);
    font-size: 12.5px;
    line-height: 18.5px;
  }
  .contact-company {
    font-weight: 700;
    font-size: 13.5px;
    letter-spacing: 1.6px;
    color: var(--text-dark);
    margin-bottom: 10px;
  }
  .contact .divider { padding: 0 8px; }
</style>
</head>
<body>
  <main class="letterhead">
    <svg class="corner-accent" width="122" height="120" viewBox="0 0 122 120" aria-hidden="true">
      <polygon points="0,0 122,0 0,120" fill="var(--accent-blue)"/>
    </svg>

    <div class="portrait-frame">
      <div class="portrait" role="img" aria-label="Portrait photograph of Tobias in a dark suit and tie"></div>
    </div>

    <header class="masthead">
      <p class="masthead-kicker">TOBIAS'S QUARTERLY</p>
      <h1 class="masthead-title">GROWTH LETTER</h1>
    </header>

    <div class="footer-rule"></div>

    <div class="brand">
      <div class="brand-dot"></div>
      <div class="brand-name">BRV Solutions</div>
    </div>

    <address class="contact">
      <div class="contact-company">BRV SOLUTIONS WLL</div>
      <div>P.O. Box 51742, Manama, Kingdom of Bahrain</div>
      <div>+973 3000 0147<span class="divider">|</span>tobias@brvsolutions.example</div>
      <div>www.brvsolutions.example</div>
    </address>
  </main>
</body>
</html>
```